Tavo Rojo --- New BBQ Marinade

We are launching a new chimichurri marinade sauce called TAVO ROJO (It is an argentinian BBQ meat marinade). It can be used on all meats (Chicken Pork Beef) but is mainly used on Skirt Steak (Churrasco). We are going to be packaging this product mainly in Mason Jar sized containers. The label will be 10 in by 3 inches and the size 16 oz. We need the bottle to pop on the shelf including reds and yellows etc. We would like to incorporate meat into the label either in cartoon form or in live picture also either in whole cow/pig/chicken or slices of meat etc. Will also need Shake Well and Refrigerate After Opening on the Label.

Our product has no preservatives, is all natural, vegetarian and gluten free so something displaying that information would be nice. I have attached our supermarket logo which if possible we would like the name of the product "Tavo Rojo" to resemble if possible as we do have Logo recognition currently. Also we will need room on the label for UPC, Ingredients and our "story" we are looking for mainly the front image and coloring scheme. The ingredients if you would like to add them to your design is Parsley, oregano, bay leaves garlic, oil, vinegar, and pimento peppers. Any questions you may have or additional details please do not hesitate to contact us lena@tavomercado.example.

Target Market(s)

Green Basket, Supermarkets, Meat Markets, BBQ Stores

Font styles to use
Serif
Sans Serif
Decorative

Colors
ec1f27
fbed22

Requirements
Must have
• Must have pop of color....screaming buy me....relation to meat

```html
<!DOCTYPE html>
<html lang="en">
<head>
<meta charset="utf-8">
<title>Tavo Rojo — BBQ Meat Marinade Label</title>
<link rel="stylesheet" href="https://fonts.googleapis.com/css2?family=Abril+Fatface&family=Oswald:wght@600;700&display=swap">
<style>
  :root {
    --label-red: #ec1f27;
    --label-yellow: #fbed22;
    --ink-black: #1a1a1a;
    --gold-dark: #8a5a1c;
    --gold-mid: #c8923a;
    --gold-light: #f3d88a;
    --ribbon-text: #f7d873;
    --ribbon-tail: #6e4212;
    --paper: #ffffff;
    --jar-glass: #eef0f2;
    --jar-edge: #b8bcc0;
  }
  html, body {
    margin: 0;
    padding: 0;
    width: 1200px;
    height: 848px;
    overflow: hidden;
    background: var(--paper);
  }
  .label-canvas {
    display: block;
    width: 1200px;
    height: 848px;
  }
  .brand-name {
    font-family: "Abril Fatface", "Times New Roman", serif;
    fill: var(--label-red);
  }
  .brand-name-shadow {
    font-family: "Abril Fatface", "Times New Roman", serif;
    fill: var(--ink-black);
  }
  .ribbon-title {
    font-family: "Oswald", "Arial Narrow", sans-serif;
    font-weight: 700;
    fill: var(--ribbon-text);
  }
  .claim-text {
    font-family: "Oswald", "Arial Narrow", sans-serif;
    font-weight: 600;
    fill: var(--paper);
  }
</style>
</head>
<body>
<svg class="label-canvas" viewBox="0 0 1200 848" xmlns="http://www.w3.org/2000/svg">
  <defs>
    <linearGradient id="gold-frame" x1="0" y1="0" x2="1" y2="0">
      <stop offset="0" stop-color="var(--gold-dark)"/>
      <stop offset="0.35" stop-color="var(--gold-light)"/>
      <stop offset="0.6" stop-color="var(--gold-mid)"/>
      <stop offset="1" stop-color="var(--gold-dark)"/>
    </linearGradient>
    <linearGradient id="ribbon-fill" x1="0" y1="0" x2="1" y2="0">
      <stop offset="0" stop-color="#7a4a16"/>
      <stop offset="0.3" stop-color="#c08a3e"/>
      <stop offset="0.65" stop-color="#9c6424"/>
      <stop offset="1" stop-color="#d8a256"/>
    </linearGradient>
    <radialGradient id="sunburst-glow" cx="0.5" cy="0.75" r="0.75">
      <stop offset="0" stop-color="#fff6d8"/>
      <stop offset="0.6" stop-color="#fde3c0"/>
      <stop offset="1" stop-color="#ffffff"/>
    </radialGradient>
    <linearGradient id="meat-tones" x1="0" y1="0" x2="1" y2="1">
      <stop offset="0" stop-color="#e8a2a6"/>
      <stop offset="1" stop-color="#f6d6d2"/>
    </linearGradient>
    <linearGradient id="jar-glass-fill" x1="0" y1="0" x2="1" y2="0">
      <stop offset="0" stop-color="#f7f8f9"/>
      <stop offset="0.5" stop-color="var(--jar-glass)"/>
      <stop offset="1" stop-color="#f7f8f9"/>
    </linearGradient>
    <path id="ribbon-curve" d="M 462 462 Q 640 470 838 420"/>
  </defs>

  <!-- Wrap band -->
  <g class="wrap-band">
    <rect x="150" y="257" width="955" height="96" fill="var(--label-red)"/>
    <rect class="animal-art cow" x="200" y="266" width="118" height="78" rx="6" fill="#f3c7c8" role="img" aria-label="Illustration of a standing dairy cow"/>
    <rect class="animal-art rooster" x="325" y="266" width="52" height="82" rx="6" fill="#f6dcdc" role="img" aria-label="Illustration of a white rooster"/>
    <rect class="animal-art sheep" x="855" y="268" width="80" height="72" rx="6" fill="#f6dcdc" role="img" aria-label="Illustration of a white sheep"/>
    <rect class="animal-art pig" x="965" y="278" width="118" height="52" rx="6" fill="#f6dcdc" role="img" aria-label="Illustration of a pig"/>
  </g>

  <!-- Shield -->
  <g class="label-shield">
    <path class="shield-backing" d="M 430 78 L 828 78 Q 830 100 845 104 L 845 430 Q 838 520 630 577 Q 422 520 413 430 L 413 104 Q 428 100 430 78 Z" fill="var(--label-yellow)" stroke="url(#gold-frame)" stroke-width="3"/>
    <path class="shield-face" d="M 413 208 Q 630 160 845 208 L 828 420 Q 800 520 630 565 Q 460 520 432 420 Z" fill="url(#gold-frame)"/>
    <path class="shield-sunburst" d="M 425 218 Q 630 176 833 218 L 817 418 Q 790 510 630 552 Q 470 510 443 418 Z" fill="url(#sunburst-glow)" role="img" aria-label="Sunburst rays in soft orange behind the product name"/>

    <path class="meat-cap-frame" d="M 528 78 L 732 78 L 732 160 Q 732 216 630 216 Q 528 216 528 160 Z" fill="url(#gold-frame)"/>
    <path class="meat-cap" d="M 536 78 L 724 78 L 724 158 Q 724 207 630 207 Q 536 207 536 158 Z" fill="var(--label-red)"/>
    <rect class="meat-art" x="552" y="92" width="156" height="100" rx="40" fill="url(#meat-tones)" role="img" aria-label="Raw beef cut and whole raw chicken"/>

    <text class="brand-name-shadow" x="634" y="315" text-anchor="middle" font-size="84" textLength="228" lengthAdjust="spacingAndGlyphs">TAVO</text>
    <text class="brand-name" x="630" y="312" text-anchor="middle" font-size="84" textLength="228" lengthAdjust="spacingAndGlyphs">TAVO</text>
    <text class="brand-name-shadow" x="634" y="389" text-anchor="middle" font-size="84" textLength="196" lengthAdjust="spacingAndGlyphs">ROJO</text>
    <text class="brand-name" x="630" y="386" text-anchor="middle" font-size="84" textLength="196" lengthAdjust="spacingAndGlyphs">ROJO</text>
  </g>

  <!-- Claim seal (sits beneath the ribbon) -->
  <g class="claim-seal">
    <circle cx="640" cy="524" r="60" fill="var(--label-red)"/>
    <g class="claim-text" font-size="14" text-anchor="middle" transform="rotate(-16 640 524)">
      <text x="640" y="504">No preservatives,</text>
      <text x="640" y="521">is all natural</text>
      <text x="640" y="538">Vegetarian and</text>
      <text x="640" y="555">Gluten FREE</text>
    </g>
  </g>

  <!-- Ribbon -->
  <g class="title-ribbon">
    <path class="ribbon-tail-left" d="M 405 398 Q 420 388 450 400 L 452 446 Q 425 436 410 444 Q 398 420 405 398 Z" fill="var(--ribbon-tail)"/>
    <path class="ribbon-tail-right" d="M 815 398 L 850 408 L 852 456 Q 835 464 815 458 Z" fill="var(--ribbon-tail)"/>
    <path class="ribbon-band" d="M 432 412 Q 640 440 842 380 L 845 436 Q 640 496 440 472 Z" fill="url(#ribbon-fill)"/>
    <text class="ribbon-title" font-size="40">
      <textPath href="#ribbon-curve" startOffset="50%" text-anchor="middle">BBQ Meat Marinade</textPath>
    </text>
  </g>

  <!-- Jar previews -->
  <g class="jar-previews">
    <rect class="jar-preview back" x="403" y="595" width="116" height="203" rx="22" fill="url(#jar-glass-fill)" stroke="var(--jar-edge)" stroke-width="1.5" role="img" aria-label="Mason jar seen from the back with the wrap band of animals"/>
    <rect class="jar-preview front" x="757" y="595" width="116" height="203" rx="22" fill="url(#jar-glass-fill)" stroke="var(--jar-edge)" stroke-width="1.5" role="img" aria-label="Mason jar seen from the front with the shield label"/>
  </g>
</svg>
</body>
</html>
```